Verpackungen für Vertrieb von Küchen- und Haushaltsartikeln
Zielgruppe
Wir vertreiben Küchen- und Haushaltsartikel über verschiedene Online-Plattformen. Unsere Produkten bieten Qualität im mittleren Preissegment. Unsere Zielgruppe sind deutsche Durchschnittshaushalte Mit Interesse in den Bereichen Kochen und Gesundheit.
Aufgabenstellung
Wir vertreiben eine Halterung für gespülte Flaschen von Perlo Quell. Diese werden kopfüber in die Klarovithalterung gestellt, um abzutropfen. Unten liegt eine Silikoneinlage ein, um das Tropfwasser aufzunehmen.
Bilder stelle ich mit ein. Vergleichsprodukte sind dies:
https://www.marktkorb-versand.de/s?k=Q52R19KTX4&ref=404_search
https://www.marktkorb-versand.de/s?k=Q52TJH47MP&__mk_de_DE=%C3%85M%C3%85%C5%BD%C3%95%C3%91&ref=nb_sb_noss
Unser Produkt ist allerdings aus Klarovit. Die Maße der Packung betragen: BxHxT = 30,00cm x 15,00 cm x 20,00 cm
Vorhandenes Logo sollte berücksichtigt werden. Wir haben weitere Projekte, die wir ggf. vergeben möchten.

```html
<!DOCTYPE html>
<html lang="de">
<head>
<meta charset="utf-8">
<title>Tropfano – Verpackung Flaschenhalterung</title>
<link rel="stylesheet" href="https://fonts.googleapis.com/css2?family=Exo+2:wght@400;600&family=Nunito:wght@400;600&family=Allura&display=swap">
<style>
  :root {
    --brand-blue: #2b96dd;
    --line-blue: #5cb0ea;
    --panel: #ffffff;
    --stage: #eef1f4;
    --edge: #d6dce2;
  }
  * { margin: 0; padding: 0; box-sizing: border-box; }
  html, body { width: 1200px; height: 1200px; overflow: hidden; }
  body {
    position: relative;
    background: var(--stage);
    font-family: "Nunito", sans-serif;
    color: var(--brand-blue);
  }
  .panel {
    position: absolute;
    background: var(--panel);
    border: 1px solid var(--edge);
    overflow: hidden;
  }
  .panel--top   { left: 510px; top: 200px; width: 540px; height: 360px; }
  .panel--front { left: 510px; top: 560px; width: 540px; height: 270px; }
  .panel--side  { left: 150px; top: 560px; width: 360px; height: 270px; }

  .wordmark {
    font-family: "Exo 2", sans-serif;
    font-weight: 600;
    color: var(--brand-blue);
    letter-spacing: 0.5px;
    line-height: 1;
  }

  /* top panel */
  .top-illustration {
    position: absolute; left: 24px; top: 60px; width: 250px; height: 260px;
    background: linear-gradient(160deg, #f4f9fe, #e3f0fb);
    border-radius: 4px;
  }
  .top-brand { position: absolute; left: 300px; top: 48px; width: 220px; }
  .top-brand .wordmark { font-size: 46px; }
  .top-brand .claim { margin-top: 8px; font-size: 12px; line-height: 1.35; }
  .top-script {
    position: absolute; left: 300px; top: 170px; width: 225px;
    font-family: "Allura", cursive; font-size: 27px; line-height: 1.15;
  }

  /* front panel */
  .front-brand { position: absolute; left: 0; top: 40px; width: 100%; text-align: center; }
  .front-brand .wordmark { font-size: 64px; }
  .front-brand .claim { margin-top: 10px; font-size: 12px; line-height: 1.4; font-style: italic; }
  .badges {
    position: absolute; left: 0; bottom: 34px; width: 100%;
    display: flex; justify-content: center; gap: 26px;
  }
  .badge {
    width: 58px; height: 58px; border-radius: 50%;
    border: 2px solid var(--brand-blue);
  }

  /* side panel */
  .side-brand { position: absolute; left: 0; top: 82px; width: 100%; text-align: center; }
  .side-brand .wordmark { font-size: 42px; }
  .side-brand .claim { margin-top: 8px; font-size: 8px; line-height: 1.4; }

  .corner-mark { position: absolute; right: 70px; bottom: 70px; }
  .corner-mark .wordmark { font-size: 54px; }
</style>
</head>
<body>

  <section class="panel panel--top" aria-label="Deckel">
    <div class="top-illustration" role="img" aria-label="Linienzeichnung: zwei Glasflaschen kopfüber in der Klarovithalterung"></div>
    <div class="top-brand">
      <div class="wordmark">Tropfano</div>
      <p class="claim">Premium Flaschenhalterung aus Klarovit<br>für Perlo Quell Glasflaschen</p>
    </div>
    <p class="top-script">Das perfekte Zubehör für<br>jeden Perlo Quell Lumen</p>
  </section>

  <section class="panel panel--side" aria-label="Seitenfläche">
    <div class="side-brand">
      <div class="wordmark">Tropfano</div>
      <p class="claim">Flaschenhalterung aus Klarovit<br>mit Abtropf-Silikoneinlage für Perlo Quell Glasflaschen</p>
    </div>
  </section>

  <section class="panel panel--front" aria-label="Vorderseite">
    <div class="front-brand">
      <div class="wordmark">Tropfano</div>
      <p class="claim">Flaschenhalterung aus Klarovit<br>mit Abtropf-Silikoneinlage für Perlo Quell Glasflaschen</p>
    </div>
    <div class="badges">
      <span class="badge"></span>
      <span class="badge"></span>
      <span class="badge"></span>
    </div>
  </section>

  <div class="corner-mark"><div class="wordmark">Tropfano</div></div>

</body>
</html>
```